Customizable Form Generation Website

This will be a place for users to quickly generate numerous forms from a categorized list. As the forms are templates with field variables, the site must be able to substitute ‘real data’ for template variable data. This tool will allow for quick custom forms on-demand.

The landing page is attached. We need the User Experience and User Interface solved for us.

EXAMPLE:
——————————————————————-
Dear {{PatientFirstName}},

Please come back for an examination on {{SelectedDate}} with Doctor {{SelectedProvider}}.

Sincerely,

{{SelectedAuthor}}
——————————————————————-

Coming to the Forms Landing Page, the user will see the forms available to select. The user will then click to select a form.

At some point, the user must resolve the variables in the form. For instance, there are the following variables in the above example: PatientFirstName, SelectedDate, SelectedProvider, and SelectedAuthor. We must give the user a chance to select the values for these variables. Using a dropdown combobox will probably work for most. Getting a date selector will be required if the variable happens to contain the string 'date'.

Is it best to preselect common variables before opening the form, or is it best to dynamically scan the template, then give the user the option to give values to each variable found?

The design must include a way for users to upload additional forms. Forms will most probably be PDF, .DOC, .TXT files. This allows users to develop simple or fancy forms of their choosing., then simply drop them into the site for future use.

The design must include a way for users to create new forms. The form creation tool must present to the user the list of predefined variables like {{PatientLastName}} for easy insertion into the form writer. Anytime "{{}}" are used, developers will recognize that as a variable that needs to be resolved.

The forms will be separated into categories as follows:

OFFICE:
- Letterhead
- Sign-In Sheet
- Fax Cover Sheet
SCHEDULER:
- Appointment Reminder
- Missed Appointment Policy
PATIENT:
- Intake Form
- Patient Discharge
- Return to Work or School
- Excuse Slip
- Consent to Treat a Minor
- Verify Non-Pregnancy
RELEASE:
- Health Information Release Form
- X-Ray Release Form
CERTIFICATES:
- Certificate of Care
- Disability Certificate
INSURANCE:
- Authorization to Bill Insurance
- Assignment Authorization
OTHER:
- Free Massage
- Free Vitamins

The design must include a way to add/customize categories. Categories are for organizing the forms logically.

We welcome ANY questions to help understand the requirements.

Good luck!

Industry/Entity Type

Healthcare

Number of Pages Required

3 page

Requirements
Must have
• Must Follow VELLUM PATTERN standards
Nice to have
• Great User Experience. Simple, Fast, Clever.
Should not have
• nothing to add here

```html
<!DOCTYPE html>
<html lang="en">
<head>
<meta charset="utf-8">
<title>Vesperline — Forms</title>
<link href="https://fonts.googleapis.com/css2?family=Rubik:wght@400;500;700&display=swap" rel="stylesheet">
<style>
  :root {
    --topbar: #0d1a2b;
    --ink: #1b2536;
    --muted: #6b717a;
    --field-bg: #f4f4f4;
    --field-border: #d9d9d9;
    --panel-border: #dcdcdc;
    --sidebar-bg: #f4f4f4;
    --brand-blue: #1c5a8f;
    --navy: #13213d;
    --white: #ffffff;
  }
  * { box-sizing: border-box; margin: 0; padding: 0; }
  html, body { width: 1200px; height: 632px; overflow: hidden; background: var(--white); }
  body { position: relative; font-family: "Rubik", Arial, sans-serif; color: var(--ink); }

  .topbar { position: absolute; left: 0; top: 0; width: 1200px; height: 37.5px; background: var(--topbar); color: var(--white); }
  .brand { position: absolute; left: 50px; top: 10px; font-size: 14px; font-weight: 700; }
  .topbar-link { position: absolute; top: 13px; font-size: 9.5px; font-weight: 500; }

  .mainnav { position: absolute; left: 0; top: 37.5px; width: 1190px; height: 45px; border-bottom: 1px solid #e6e6e6; }
  .nav-item { position: absolute; top: 15px; font-size: 10.8px; color: var(--ink); }
  .nav-item.active { font-weight: 500; }
  .nav-item.active::after { content: ""; position: absolute; left: 0; right: -1px; top: 28px; height: 2px; background: var(--ink); }

  .page-title { position: absolute; left: 196px; top: 111px; font-size: 25px; font-weight: 400; }
  .btn-create { position: absolute; left: 866px; top: 109px; width: 138px; height: 37.5px; background: var(--brand-blue); color: var(--white); font-size: 9.5px; font-weight: 500; display: flex; align-items: center; justify-content: center; }

  .categories { position: absolute; left: 196px; top: 164px; width: 208px; height: 386px; }
  .category { position: relative; background: var(--sidebar-bg); height: 47px; border-top: 1px solid #e4e4e4; }
  .category.open { height: 104px; border-top: none; }
  .category-name { position: absolute; left: 18px; top: 16px; font-size: 12px; }
  .category.open .category-name { top: 15px; font-weight: 500; }
  .toggle { position: absolute; left: 182px; top: 14px; font-size: 12px; font-weight: 500; }
  .form-list { position: absolute; left: 18px; top: 41px; list-style: none; font-size: 9.5px; color: var(--muted); line-height: 18.7px; }
  .form-list .current { color: var(--ink); font-weight: 500; }

  .btn-upload { position: absolute; left: 196px; top: 562px; width: 206px; height: 40px; border: 1px solid var(--ink); font-size: 9.5px; font-weight: 500; display: flex; align-items: center; justify-content: center; }

  .form-panel { position: absolute; left: 421px; top: 164px; width: 583px; height: 438px; border: 1px solid var(--panel-border); }
  .letterhead { position: absolute; left: 0; top: 0; width: 100%; height: 97px; border-bottom: 1px solid var(--panel-border); }
  .logo-box { position: absolute; left: 17px; top: 17px; width: 62.5px; height: 62.5px; background: var(--navy); color: var(--white); font-size: 15px; display: flex; align-items: center; justify-content: center; }
  .company-name { position: absolute; left: 90px; top: 40px; font-size: 15px; }

  .form-title { position: absolute; left: 17px; top: 119px; font-size: 20px; font-weight: 400; }
  .field-label { position: absolute; font-size: 10.5px; }
  .field { position: absolute; width: 265px; height: 35px; background: var(--field-bg); border: 1px solid var(--field-border); font-size: 9.5px; color: var(--muted); display: flex; align-items: center; padding-left: 8.5px; }
  .field svg.icon { margin-right: 7px; }
  .field .caret { position: absolute; right: 9px; top: 15px; }

  .action { position: absolute; top: 394px; font-size: 9.5px; font-weight: 500; }
  .btn-download { position: absolute; left: 491px; top: 381.5px; width: 74px; height: 35px; background: var(--navy); color: var(--white); font-size: 9.5px; font-weight: 500; display: flex; align-items: center; justify-content: center; }
</style>
</head>
<body>
  <header class="topbar">
    <div class="brand">Vesperline</div>
    <span class="topbar-link" style="left:845px">Sample healthcare practice</span>
    <span class="topbar-link" style="left:1000px">Welcome back test</span>
    <span class="topbar-link" style="left:1114px">Log out</span>
  </header>

  <nav class="mainnav">
    <span class="nav-item" style="left:196px">Home</span>
    <span class="nav-item" style="left:257px">Scheduler</span>
    <span class="nav-item" style="left:340px">Patients</span>
    <span class="nav-item" style="left:414px">Encounters</span>
    <span class="nav-item" style="left:504px">Payments</span>
    <span class="nav-item" style="left:587px">Billings</span>
    <span class="nav-item" style="left:655px">Reporting</span>
    <span class="nav-item" style="left:737px">Marketing</span>
    <span class="nav-item active" style="left:819px">Forms</span>
    <span class="nav-item" style="left:883px">Lists</span>
    <span class="nav-item" style="left:938px">Admin</span>
  </nav>

  <h1 class="page-title">Category</h1>
  <div class="btn-create">Create custom form</div>

  <aside class="categories">
    <div class="category open">
      <span class="category-name">Office</span>
      <span class="toggle">–</span>
      <ul class="form-list">
        <li class="current">Letterhead</li>
        <li>Sign-In Sheet</li>
        <li>Fax Cover Sheet</li>
      </ul>
    </div>
    <div class="category"><span class="category-name">Scheduler</span><span class="toggle">+</span></div>
    <div class="category"><span class="category-name">Patient</span><span class="toggle">+</span></div>
    <div class="category"><span class="category-name">Release</span><span class="toggle">+</span></div>
    <div class="category"><span class="category-name">Certificates</span><span class="toggle">+</span></div>
    <div class="category"><span class="category-name">Insurance</span><span class="toggle">+</span></div>
    <div class="category"><span class="category-name">Other</span><span class="toggle">+</span></div>
  </aside>
  <div class="btn-upload">Upload additional forms</div>

  <main class="form-panel">
    <div class="letterhead">
      <div class="logo-box">Logo</div>
      <div class="company-name">Company name</div>
    </div>

    <h2 class="form-title">Patient Form</h2>

    <span class="field-label" style="left:17px;top:160px">Dear</span>
    <div class="field" style="left:17px;top:180px">Patient First Name</div>
    <div class="field" style="left:299px;top:180px">Patient Last Name</div>

    <span class="field-label" style="left:17px;top:234px">Please come back for an examination on</span>
    <div class="field" style="left:17px;top:253.5px">
      <svg class="icon" width="13" height="13" viewBox="0 0 13 13" fill="none" stroke="#6b717a" stroke-width="1.1"><rect x="1" y="2" width="11" height="10" rx="1"/><line x1="1" y1="5" x2="12" y2="5"/><line x1="4" y1="0.5" x2="4" y2="3"/><line x1="9" y1="0.5" x2="9" y2="3"/></svg>
      SelectedDate
      <svg class="caret" width="7" height="5" viewBox="0 0 7 5"><path d="M0 0h7L3.5 5z" fill="#444"/></svg>
    </div>
    <span class="field-label" style="left:299px;top:234px">With Doctor</span>
    <div class="field" style="left:299px;top:253.5px">
      <svg class="icon" width="12" height="13" viewBox="0 0 12 13" fill="none" stroke="#6b717a" stroke-width="1.1"><circle cx="6" cy="4" r="3"/><path d="M1 12.5c0-3 2.2-5 5-5s5 2 5 5"/></svg>
      SelectedProvider
      <svg class="caret" width="7" height="5" viewBox="0 0 7 5"><path d="M0 0h7L3.5 5z" fill="#444"/></svg>
    </div>

    <span class="field-label" style="left:17px;top:308px">Sincerely,</span>
    <div class="field" style="left:17px;top:327.5px">
      SelectedAuthor
      <svg class="caret" width="7" height="5" viewBox="0 0 7 5"><path d="M0 0h7L3.5 5z" fill="#444"/></svg>
    </div>

    <span class="action" style="left:17px">Save</span>
    <span class="action" style="left:444px">Preview</span>
    <div class="btn-download">Download</div>
  </main>
</body>
</html>
```